Mandala Postcard Design

I am in need of a postcard to hand out at a Psychic Fair. I envision the card to having half-of-a Mandala (from my Facebook folder), touched up a bit to make it vibrant and bold. Others vendors will have cards w/photographic backgrounds doing yoga. I'd like mine to stand out for it's line-drawn "cartoonish" nature, solid-color nature. The wording would be my basic contact info and a short description ... something like: "Experience the Magic of Mandala Making ... Next Class will be held: (open space for writing, no lines) The art is contained in this Facebook folder. Lots to choose from, with my favorites being the stronger outlined designs.

https://www.sketchnook.example/Brightloom/media_set?set=a.20262926615637197.2184852941.783542196&type=3
Updates

I just uploaded a few new drawings that might work better, since they are more round. I want to minimize the white space, for instance, avoid having the left & right corners empty. Another idea could be to use 1/4 mandalas in the corners. I'm ready to make a decision. I want it to look great, but as I gain drawing experience, I'll need to update my cards. Thanks! I'm not sure if this the place for this comment, but I'll also be needing a DVD label for my tutorials, and a front page design for a mandala coloring book.

Target Market(s)

Primarily women interested in metaphysical, psychic, meditation, reiki and a basic interest in art.

Font styles to use
Serif
Sans Serif

Requirements
Should not have
• Should not be on a dark card, really should be a plain white background, it seems, in order to stand out.

```html
<!DOCTYPE html>
<html lang="en">
<head>
<meta charset="utf-8">
<title>Experience the Magic of Mandala Making</title>
<link rel="stylesheet" href="https://fonts.googleapis.com/css2?family=Noto+Sans:wght@400&display=swap">
<style>
  :root {
    --card-white: #ffffff;
    --ink: #1c0a12;
    --title-glow: #d6336c;
    --mandala-pink: #f3a9bf;
    --mandala-yellow: #f5ec9a;
    --mandala-blue: #a9d4ea;
  }
  html, body {
    margin: 0;
    padding: 0;
    width: 1200px;
    height: 846px;
    overflow: hidden;
    background: var(--card-white);
  }
  .postcard {
    position: relative;
    width: 1200px;
    height: 846px;
    background: var(--card-white);
    font-family: "Noto Sans", Verdana, sans-serif;
    color: var(--ink);
    overflow: hidden;
  }
  .mandala-art {
    position: absolute;
    left: 0;
    top: 0;
    width: 1200px;
    height: 846px;
    background:
      radial-gradient(ellipse 22% 30% at 50% 50%, var(--mandala-yellow) 0%, rgba(245,236,154,0.85) 55%, rgba(245,236,154,0) 100%),
      radial-gradient(ellipse 40% 46% at 50% 50%, var(--mandala-pink) 30%, rgba(243,169,191,0.55) 65%, rgba(243,169,191,0) 100%),
      radial-gradient(ellipse 56% 60% at 50% 50%, rgba(169,212,234,0.9) 45%, rgba(169,212,234,0.35) 80%, rgba(255,255,255,0) 100%);
    opacity: 0.75;
  }
  .headline {
    position: absolute;
    left: 0;
    width: 100%;
    margin: 0;
    text-align: center;
    font-weight: 400;
    text-shadow: 3px 3px 0 var(--title-glow);
    line-height: 1;
    white-space: nowrap;
  }
  .headline-lead {
    top: 35px;
    font-size: 88px;
    letter-spacing: 3px;
  }
  .headline-main {
    top: 406px;
    font-size: 114px;
    letter-spacing: 1px;
  }
  .next-class {
    position: absolute;
    left: 42px;
    top: 774px;
    margin: 0;
    font-size: 42px;
    letter-spacing: 3px;
    line-height: 1;
    white-space: nowrap;
  }
</style>
</head>
<body>
  <main class="postcard">
    <div class="mandala-art" role="img" aria-label="Hand-drawn mandala in pink, yellow and blue filling the card behind the text"></div>
    <h1 class="headline headline-lead">Experience the Magic of</h1>
    <h2 class="headline headline-main">Mandala Making</h2>
    <p class="next-class">Next Class Starts:</p>
  </main>
</body>
</html>
```